High-end construction company needs a business card design

We need a modern looking business card that draws people in, is memorable and looks so good people will want to sick it on their fridges.
On the first side what is needed are:
Logo
My name - Tomas Brevik
Title - Managing Director
Website - www.kelvora.co.uk
Email - tomas@kelvora.co.uk
Telephone - 020 4917 2365
Mobile - 07845139072
On the back side was is needed is a list of all the services we provide:
-Kitchen Renovations
-Bathroom Renovations
-House Renovations
-Garage Conversions
-Extensions
-Loft Conversions
-Conservatories
-Carpentry
-Tiling
-Electrical
-Plumbing & Heating
-Bricklaying
-Landscaping
-Decorating
-Plastering
We would like the colours to be the same shades as on the logo with grey or black for the words.
Target Market(s)
Anyone who needs building work done
Contact Information for Business Card
This business card is for a construction company which strives to deliver excellent service and quality.
The look and feel of the card should represent this.
Requirements
Must have
- On the first side what is needed are:
Logo
My name - Tomas Brevik
Title - Managing Director
Website - www.kelvora.co.uk
Email - tomas@kelvora.co.uk
Telephone - 020 4917 2365
Mobile - 07845139072
Nice to have
- Cool looking features

```html
<!DOCTYPE html>
<html lang="en">
<head>
<meta charset="utf-8">
<title>Kelvora Construction – Business Card</title>
<link href="https://fonts.googleapis.com/css2?family=Montserrat:wght@500;600;700;800&family=Open+Sans:wght@400;600&display=swap" rel="stylesheet">
<style>
  :root {
    --stage: #2b2b2b;
    --card-dark: #1c1c1c;
    --card-black: #101010;
    --green: #6cc04a;
    --green-light: #8ad35f;
    --green-deep: #3f8a2a;
    --text-light: #f2f2f2;
    --text-muted: #cfcfcf;
    --text-dark: #161616;
  }
  * { margin: 0; padding: 0; box-sizing: border-box; }
  html, body { width: 1200px; height: 900px; overflow: hidden; }
  body {
    background: var(--stage);
    font-family: "Open Sans", Arial, sans-serif;
    display: flex;
    align-items: center;
    justify-content: center;
    gap: 40px;
  }
  .card {
    position: relative;
    width: 540px;
    height: 320px;
    border-radius: 18px;
    overflow: hidden;
    box-shadow: 0 18px 40px rgba(0,0,0,.45);
  }

  /* ---------- Front ---------- */
  .card-front { background: var(--card-dark); }
  .front-band {
    position: absolute; left: 0; right: 0; bottom: 0;
    height: 22px; background: var(--green);
  }
  .holder { position: absolute; left: 32px; top: 44px; }
  .holder-name {
    font-family: "Montserrat", sans-serif;
    font-weight: 600; font-size: 21px; letter-spacing: 1.5px;
    color: var(--text-light); text-transform: uppercase;
  }
  .holder-title {
    margin-top: 4px;
    font-family: "Montserrat", sans-serif;
    font-weight: 500; font-size: 11px; letter-spacing: 2px;
    color: var(--green); text-transform: uppercase;
  }
  .divider {
    position: absolute; top: 128px; height: 2px; background: var(--green);
  }
  .divider-left { left: 0; width: 250px; }
  .divider-right { left: 500px; width: 40px; }

  .logo {
    position: absolute; left: 262px; top: 104px; width: 230px;
    text-align: center; color: var(--green);
    font-family: "Montserrat", sans-serif; font-weight: 800;
  }
  .logo-name { font-size: 40px; letter-spacing: 2px; line-height: 1; }
  .logo-sub { font-size: 11.5px; letter-spacing: 3.2px; margin-top: 5px; }
  .logo-mark {
    display: inline-block; width: 10px; height: 10px;
    background: var(--green); margin-left: 6px; vertical-align: middle;
  }

  .contact-list { position: absolute; list-style: none; font-size: 13px; color: var(--text-muted); }
  .contact-list li { display: flex; align-items: center; gap: 9px; height: 22px; }
  .contact-list svg { width: 13px; height: 13px; fill: var(--green); flex: none; }
  .contact-phones { left: 32px; top: 238px; }
  .contact-online { right: 30px; top: 238px; }
  .contact-online li { justify-content: flex-end; }

  /* ---------- Back ---------- */
  .card-back { background: linear-gradient(135deg, var(--green-light), var(--green) 60%, #5aae3c); }
  .back-shape { position: absolute; inset: 0; width: 100%; height: 100%; }
  .back-logo { left: 290px; top: 36px; }
  .back-logo .logo-name { font-size: 38px; }

  .service-list {
    position: absolute; list-style: none;
    font-size: 13px; font-weight: 600; color: var(--text-dark);
  }
  .service-list li { display: flex; align-items: center; gap: 7px; height: 22px; }
  .tick { width: 13px; height: 13px; flex: none; }
  .services-a { left: 24px; top: 80px; }
  .services-b { left: 200px; top: 142px; }
  .services-c { left: 372px; top: 206px; }
</style>
</head>
<body>

<!-- Front side -->
<section class="card card-front" aria-label="Business card front">
  <div class="holder">
    <div class="holder-name">Tomas Brevik</div>
    <div class="holder-title">Managing Director</div>
  </div>

  <div class="divider divider-left"></div>
  <div class="divider divider-right"></div>

  <div class="logo">
    <div class="logo-name">KELVORA<span class="logo-mark"></span></div>
    <div class="logo-sub">CONSTRUCTION LTD</div>
  </div>

  <ul class="contact-list contact-phones">
    <li>
      <svg viewBox="0 0 24 24" aria-hidden="true"><path d="M6.6 10.8a15.1 15.1 0 0 0 6.6 6.6l2.2-2.2a1 1 0 0 1 1-.25 11.4 11.4 0 0 0 3.6.57 1 1 0 0 1 1 1V20a1 1 0 0 1-1 1A17 17 0 0 1 3 4a1 1 0 0 1 1-1h3.5a1 1 0 0 1 1 1c0 1.25.2 2.45.57 3.57a1 1 0 0 1-.25 1z"/></svg>
      020 4917 2365
    </li>
    <li>
      <svg viewBox="0 0 24 24" aria-hidden="true"><path d="M7 1h10a2 2 0 0 1 2 2v18a2 2 0 0 1-2 2H7a2 2 0 0 1-2-2V3a2 2 0 0 1 2-2zm0 3v14h10V4zm5 15.2a1 1 0 1 0 0 2 1 1 0 0 0 0-2z"/></svg>
      07845139072
    </li>
  </ul>

  <ul class="contact-list contact-online">
    <li>
      tomas@kelvora.co.uk
      <svg viewBox="0 0 24 24" aria-hidden="true"><path d="M2 5h20v14H2zm2 2v.5l8 5 8-5V7zm0 2.9V17h16V9.9l-8 5z"/></svg>
    </li>
    <li>
      www.kelvora.co.uk
      <svg viewBox="0 0 24 24" aria-hidden="true"><path d="M12 2a10 10 0 1 0 0 20 10 10 0 0 0 0-20zm6.9 9h-3a15 15 0 0 0-1.2-5.6A8 8 0 0 1 18.9 11zM12 4.1c.9 1.2 1.8 3.5 1.9 6.9h-3.8C10.2 7.6 11.1 5.3 12 4.1zM9.3 5.4A15 15 0 0 0 8.1 11h-3a8 8 0 0 1 4.2-5.6zM5.1 13h3a15 15 0 0 0 1.2 5.6A8 8 0 0 1 5.1 13zm6.9 6.9c-.9-1.2-1.8-3.5-1.9-6.9h3.8c-.1 3.4-1 5.7-1.9 6.9zm2.7-1.3a15 15 0 0 0 1.2-5.6h3a8 8 0 0 1-4.2 5.6z"/></svg>
    </li>
  </ul>

  <div class="front-band"></div>
</section>

<!-- Back side -->
<section class="card card-back" aria-label="Business card back">
  <svg class="back-shape" viewBox="0 0 540 320" preserveAspectRatio="none" aria-hidden="true">
    <path d="M0 0H540V206C430 178 330 120 210 80C130 54 60 36 0 30Z" fill="#2a5e1e"/>
    <path d="M0 0H540V194C430 166 330 110 210 70C130 44 60 26 0 20Z" fill="var(--card-black)"/>
  </svg>

  <div class="logo back-logo">
    <div class="logo-name">KELVORA<span class="logo-mark"></span></div>
    <div class="logo-sub">CONSTRUCTION LTD</div>
  </div>

  <svg width="0" height="0" style="position:absolute" aria-hidden="true">
    <symbol id="tick" viewBox="0 0 16 16">
      <circle cx="8" cy="8" r="6.8" fill="none" stroke="#161616" stroke-width="1.4"/>
      <path d="M4.8 8.2l2.2 2.2 4.2-4.6" fill="none" stroke="#161616" stroke-width="1.6" stroke-linecap="round" stroke-linejoin="round"/>
    </symbol>
  </svg>

  <ul class="service-list services-a">
    <li><svg class="tick"><use href="#tick"/></svg>Kitchen Renovations</li>
    <li><svg class="tick"><use href="#tick"/></svg>Bathroom Renovations</li>
    <li><svg class="tick"><use href="#tick"/></svg>House Renovations</li>
    <li><svg class="tick"><use href="#tick"/></svg>Garage Conversions</li>
    <li><svg class="tick"><use href="#tick"/></svg>Extensions</li>
  </ul>

  <ul class="service-list services-b">
    <li><svg class="tick"><use href="#tick"/></svg>Loft Conversions</li>
    <li><svg class="tick"><use href="#tick"/></svg>Conservatories</li>
    <li><svg class="tick"><use href="#tick"/></svg>Carpentry</li>
    <li><svg class="tick"><use href="#tick"/></svg>Tiling</li>
    <li><svg class="tick"><use href="#tick"/></svg>Electrical</li>
  </ul>

  <ul class="service-list services-c">
    <li><svg class="tick"><use href="#tick"/></svg>Plumbing &amp; Heating</li>
    <li><svg class="tick"><use href="#tick"/></svg>Bricklaying</li>
    <li><svg class="tick"><use href="#tick"/></svg>Landscaping</li>
    <li><svg class="tick"><use href="#tick"/></svg>Decorating</li>
    <li><svg class="tick"><use href="#tick"/></svg>Plastering</li>
  </ul>
</section>

</body>
</html>
```